Heron Freightlines needs Bussiness cards!

Our new trucking company needs business cards!
We need the same design with two different names and emails, everything else it's the same.
I have included our original logo so we can use it for the design.
Note: the logo to be used is the o e with the buffalo on the right side, next to the letters H and F.

Target Market(s)

Trucking, refrigerated transportation, freight

Industry/Entity Type

Business

Contact Information for Business Card

Card #1:
Marcus Tellwright
marcustellwright@heronfreightlines.example
1-844-555-0193
(555)555-0178
3817 W. Tarrow Ave.
Brinmoor, NV 78599
www.heronfreightlines.example

Card#2:
Orla Brennick
orla@heronfreightlines.example
1-844-555-0193
(555)555-0178
3817 W. Tarrow Ave.
Brinmoor, NV 78599
www.heronfreightlines.example

Font styles to use
Sans Serif

Colors
0655a3
ec1f27
ffffff

Requirements
Must have
• our logo
Nice to have
• roads on background,

```html
<!DOCTYPE html>
<html lang="en">
<head>
<meta charset="utf-8">
<title>Heron Freightlines — Business Cards</title>
<link rel="stylesheet" href="https://fonts.googleapis.com/css2?family=Roboto:wght@300;400;900&display=swap">
<style>
  :root {
    --navy: #0c3a6c;
    --brand-blue: #0655a3;
    --brand-red: #ec1f27;
    --white: #ffffff;
    --ink-grey: #6b6f75;
    --rule-grey: #d9dbde;
    --backdrop: #2b2b2d;
  }
  * { box-sizing: border-box; margin: 0; padding: 0; }
  html, body {
    width: 1200px; height: 950px; overflow: hidden;
    background: var(--backdrop);
    font-family: "Roboto", Arial, sans-serif;
  }
  .sheet {
    width: 1200px; height: 950px;
    display: flex; flex-direction: column; align-items: center; justify-content: center;
    gap: 50px;
  }
  .card {
    position: relative;
    width: 700px; height: 400px;
    overflow: hidden;
    box-shadow: 0 8px 24px rgba(0,0,0,.35);
  }

  /* Front */
  .card--front { background: var(--navy); }
  .card--front .wordmark {
    position: absolute; left: 0; right: 0; top: 140px;
    text-align: center;
    font-weight: 900; font-size: 46px; color: var(--white);
    letter-spacing: -0.5px;
  }
  .card--front .website {
    position: absolute; left: 0; right: 0; top: 296px;
    text-align: center;
    font-weight: 300; font-size: 15px; color: #c9d3df;
    letter-spacing: 3.5px;
  }

  /* Back */
  .card--back { background: var(--white); }
  .card--back .wordmark {
    position: absolute; left: 38px; top: 160px;
    font-weight: 900; font-size: 31px; color: var(--brand-blue);
    letter-spacing: -0.3px;
  }
  .card--back .divider {
    position: absolute; left: 380px; top: 70px;
    width: 1px; height: 200px; background: var(--rule-grey);
  }
  .contact { position: absolute; left: 402px; top: 78px; color: var(--ink-grey); }
  .contact .name {
    font-weight: 400; font-size: 22px; color: var(--brand-blue);
    margin-bottom: 12px;
  }
  .contact .address { font-size: 13px; line-height: 18px; font-weight: 300; margin-bottom: 6px; }
  .contact .line {
    display: flex; align-items: center; gap: 8px;
    font-size: 12.5px; line-height: 20px; font-weight: 300;
  }
  .contact .line svg { width: 13px; height: 13px; flex: none; fill: var(--navy); }
  .card--back .stripes { position: absolute; left: 0; top: 0; }
  .card--back .website {
    position: absolute; right: 18px; top: 312px;
    font-size: 14px; color: var(--white); letter-spacing: 0.6px;
  }
</style>
</head>
<body>
<main class="sheet">
  <section class="card card--front">
    <div class="wordmark">Heron Freightlines</div>
    <div class="website">www.heronfreightlines.example</div>
  </section>

  <section class="card card--back">
    <div class="wordmark">Heron Freightlines</div>
    <div class="divider"></div>
    <div class="contact">
      <p class="name">Marcus Tellwright</p>
      <p class="address">3817 W. Tarrow Ave.<br>Brinmoor, NV 78599</p>
      <p class="line">
        <svg viewBox="0 0 16 16" aria-hidden="true"><path d="M3.5 1.5l2.5 0 1 3.5-1.6 1.2a9 9 0 0 0 4.4 4.4l1.2-1.6 3.5 1v2.5c0 .8-.7 1.5-1.5 1.5A12.5 12.5 0 0 1 2 3c0-.8.7-1.5 1.5-1.5z"/></svg>
        1-844-555-0193
      </p>
      <p class="line">
        <svg viewBox="0 0 16 16" aria-hidden="true"><path d="M4.5 0h7A1.5 1.5 0 0 1 13 1.5v13a1.5 1.5 0 0 1-1.5 1.5h-7A1.5 1.5 0 0 1 3 14.5v-13A1.5 1.5 0 0 1 4.5 0zM5 2v10h6V2zm3 11a1 1 0 1 0 0 2 1 1 0 0 0 0-2z"/></svg>
        (555)555-0178
      </p>
      <p class="line">
        <svg viewBox="0 0 16 16" aria-hidden="true"><path d="M1 3h14v10H1zm1.2 1.2v.3L8 8.6l5.8-4.1v-.3zM2.2 6v5.8h11.6V6L8 10.1z"/></svg>
        marcustellwright@heronfreightlines.example
      </p>
    </div>
    <svg class="stripes" width="700" height="400" viewBox="0 0 700 400" aria-hidden="true">
      <g fill="none" stroke="var(--brand-red)" stroke-width="3.5">
        <path d="M0 352 L410 352 L445 336 L700 336"/>
        <path d="M0 362 L414 362 L449 346 L700 346"/>
        <path d="M0 372 L418 372 L453 356 L700 356"/>
        <path d="M0 382 L422 382 L457 366 L700 366"/>
      </g>
      <polygon points="455,300 700,300 700,332 440,332" fill="var(--navy)"/>
      <polygon points="460,370 700,370 700,400 400,400" fill="var(--navy)"/>
    </svg>
    <div class="website">www.heronfreightlines.example</div>
  </section>
</main>
</body>
</html>
```